BRQW Coaching Website

I would like someone to design my website. I have an existing site which is really basic and needs an overhaul. I have attached a powerpoint with all the information I require. I am flexible with the design and layout and am ok with graphics being added to enhance the attractiveness of the site.

```html
<!DOCTYPE html>
<html lang="en">
<head>
<meta charset="utf-8">
<title>BRQW Coaching</title>
<link rel="stylesheet" href="https://fonts.googleapis.com/css2?family=Lato:wght@300&family=Open+Sans:wght@400&family=Arimo:wght@400&display=swap">
<style>
:root{
  --orange:#f05a28;
  --orange-dark:#ee5524;
  --blue-top:#2a8ad8;
  --blue-bottom:#1a6fc0;
  --panel-top:#f4f4f4;
  --panel-bottom:#e2e2e2;
  --ink:#111;
  --body-ink:#444;
  --footer:#2f2f2f;
  --white:#fff;
}
*{margin:0;padding:0;box-sizing:border-box}
html,body{width:1200px;height:939px;overflow:hidden;background:var(--white)}
body{position:relative;font-family:"Arimo",Arial,sans-serif}
.site-header{position:absolute;left:0;top:0;width:1200px;height:131px}
.brand{position:absolute;left:104px;top:40px;display:flex;align-items:center;gap:12px;font-family:"Arimo",Arial,sans-serif;font-size:36px;color:var(--orange)}
.brand-dot{width:22px;height:22px;background:var(--orange)}
.contact{position:absolute;right:104px;top:48px;text-align:right;font-size:15px;line-height:31px;color:var(--orange)}
.hero{position:absolute;left:0;top:131px;width:1200px;height:321px;
  background:radial-gradient(ellipse at 70% 40%,#fbf6ee 0%,#f1e6d2 35%,rgba(241,230,210,0) 65%),
  linear-gradient(90deg,#7f9960 0%,#a9b883 25%,#d9dcc0 50%,#efe1c8 75%,#d6c0a4 100%)}
.hero-title{position:absolute;left:0;right:0;top:118px;text-align:center;font-family:"Lato",sans-serif;font-weight:300;font-size:58px;color:var(--ink)}
.service-nav{position:absolute;left:104px;top:488px;width:324px}
.service-tile{position:absolute;left:0;width:324px;height:72px;padding-left:28px;display:flex;align-items:center;
  background:linear-gradient(var(--blue-top),var(--blue-bottom));color:var(--white);font-size:17px;word-spacing:3px}
.welcome{position:absolute;left:438px;top:483px;width:657px;height:245px;background:linear-gradient(var(--panel-top),var(--panel-bottom))}
.welcome h1{position:absolute;left:22px;top:18px;font-weight:400;font-size:23px;color:var(--ink);word-spacing:3px}
.welcome h1 span{color:var(--orange)}
.welcome p{position:absolute;left:22px;top:58px;width:420px;font-family:"Open Sans",sans-serif;font-size:14.5px;line-height:31px;color:var(--body-ink)}
.coach-photo{position:absolute;left:455px;top:13px;width:187px;height:218px;background:linear-gradient(160deg,#c8c2b6,#8f8678 55%,#d99a86)}
.cta{position:absolute;left:438px;top:742px;width:657px;height:72px;display:flex;align-items:center;justify-content:center;
  background:var(--orange-dark);color:var(--white);font-size:17px;word-spacing:3px}
.site-footer{position:absolute;left:0;top:844px;width:1200px;height:95px;background:var(--footer)}
.copyright{position:absolute;left:105px;top:37px;color:var(--white);font-size:15px;word-spacing:2px}
.social{position:absolute;left:940px;top:26px;display:flex;gap:1px}
.social span{width:38px;height:38px;border-radius:50%;background:var(--white)}
</style>
</head>
<body>
<header class="site-header">
  <div class="brand"><span class="brand-dot"></span>BRQW Coaching</div>
  <div class="contact">
    <div>1300 555 017</div>
    <div>Jordan.Hale@BRQWCoaching.com</div>
  </div>
</header>
<section class="hero" role="img" aria-label="Soft-focus photograph of sunlit green foliage">
  <h2 class="hero-title">Bold Reach Quiet Wins Coaching</h2>
</section>
<nav class="service-nav">
  <a class="service-tile" style="top:0">Individual Coaching (1)</a>
  <a class="service-tile" style="top:87px">Group Work (2)</a>
  <a class="service-tile" style="top:169px">Resources (3)</a>
  <a class="service-tile" style="top:254px">Inspiration Booth (5)</a>
</nav>
<section class="welcome">
  <h1>Welcome to <span>BRQW</span> Coaching</h1>
  <p>Welcome to BRQW Coaching where we put a new perspective on the way you work, live and play.<br>Through our programs you will learn new skills &amp; techniques to enable you to break through the barriers that have kept you from reaching your full potential up to now.</p>
  <div class="coach-photo" role="img" aria-label="Portrait photograph of the coach outdoors"></div>
</section>
<a class="cta">Get your free 30 minute introductory coaching session… (4)</a>
<footer class="site-footer">
  <div class="copyright">Copyright © 2014 BRQW.All rights reserved</div>
  <div class="social">
    <span aria-label="Social link 1"></span>
    <span aria-label="Social link 2"></span>
    <span aria-label="Social link 3"></span>
    <span aria-label="Social link 4"></span>
  </div>
</footer>
</body>
</html>
```